T&R Custom Homes and Remodeling Flyer

We need a new double sided flyer that showcases our service.
Our website is http://trhomesbuildco.example/
Please use the information on http://trhomesbuildco.example/about-us/ for the information in the flyer.
This handout will be used to give to our potential customers and needs to show the complete story of who we are and the services we provide. I have also attached pictures of project we have completed that should be used for the flyer.
Any other pictures can be taken from our photo gallery on the website.

Target Market(s)

Clients who want a custom home or remodel

Industry/Entity Type

Construction

Font styles to use
Serif

Requirements
Must have
• Prominent logo
• Pictures of completed projects
• Tri-fold design- eps file is attached for this
Nice to have
• Manly colors
• If you can find a tasteful way to add the picture of the owners that is great, but it should be small and is not necessary.
Should not have
• Pink/girly touches

```html
<!DOCTYPE html>
<html lang="en">
<head>
<meta charset="utf-8">
<title>T&amp;R Custom Homes and Remodeling – Tri-fold Flyer</title>
<link rel="stylesheet" href="https://fonts.googleapis.com/css2?family=Montserrat:wght@400;600;700;800&family=Open+Sans:wght@400;600&display=swap">
<style>
:root{
  --bg:#dcdcdc;
  --navy-dark:#17233a;
  --navy:#24365a;
  --navy-light:#3e5782;
  --slate-dark:#2f2f33;
  --slate:#48484d;
  --slate-light:#5d5d62;
  --band:#2a3e64;
  --band-light:#3f5a8a;
  --ink:#1b2436;
  --paper:#ffffff;
  --muted:#c9d0dc;
  --sky-top:#c6d3e2;
  --sky-bottom:#eef2f6;
}
*{box-sizing:border-box;margin:0;padding:0}
html,body{width:1200px;height:886px;overflow:hidden;background:var(--bg)}
body{position:relative;font-family:"Open Sans",Arial,sans-serif;color:var(--paper)}
.sheet{position:absolute;top:223px;width:570px;height:440px;box-shadow:0 6px 18px rgba(0,0,0,.35);overflow:hidden}
.sheet--outside{left:20px;background:linear-gradient(180deg,var(--navy-dark),var(--navy))}
.sheet--inside{left:610px;background:var(--slate)}
.panel{position:absolute;top:0;width:190px;height:440px}
.heading{font-family:"Montserrat",Arial,sans-serif;font-weight:600;font-size:9px;letter-spacing:.3px;text-align:center;display:flex;align-items:center;gap:6px;margin-bottom:6px}
.heading::before,.heading::after{content:"";flex:1;height:1px;background:rgba(255,255,255,.55)}
.body-text{font-size:5.3px;line-height:1.5;text-align:justify;color:#e7ebf2;margin-bottom:5px}
.photo{position:absolute}
.footer{position:absolute;bottom:0;left:0;width:190px;height:20px;background:linear-gradient(90deg,var(--band),var(--band-light),var(--band));display:flex;align-items:center;justify-content:center;gap:4px;font-size:6px;color:#e8edf6}
.footer .dot{width:4px;height:4px;border-radius:50%;background:#e8edf6}
.thumbs{position:absolute;display:flex;gap:6px}
.thumb{width:74px;text-align:center;font-family:"Montserrat",Arial,sans-serif;font-size:4.6px;font-weight:700;letter-spacing:.2px}
.thumb .pic{height:38px;border:2px solid #f2f2f2;margin-bottom:4px}
/* outside */
.about{left:0;padding:12px 12px 0}
.partner{font-family:"Montserrat",Arial,sans-serif;text-align:center;margin-bottom:5px}
.partner .name{font-size:9px;font-weight:400}
.partner .phone{font-size:7px;font-weight:700;display:flex;align-items:center;justify-content:center;gap:3px}
.brand{position:absolute;right:18px;top:26px;width:140px;text-align:center;font-family:"Montserrat",Arial,sans-serif;font-weight:700;color:var(--ink);font-size:11px;line-height:1.15;display:flex;align-items:center;gap:6px}
.brand .mark{width:12px;height:12px;background:var(--ink);flex:none}
.contact{left:190px;top:292px;height:128px;text-align:center;padding-top:14px;font-family:"Montserrat",Arial,sans-serif}
.contact h2{font-size:10.5px;font-weight:600;margin-bottom:8px}
.contact p{font-size:5.4px;line-height:1.5;font-family:"Open Sans",Arial,sans-serif}
.tagline{left:380px;top:292px;height:128px;border-left:1px solid rgba(255,255,255,.18);display:flex;align-items:center;justify-content:center}
.tagline h2{font-family:"Montserrat",Arial,sans-serif;font-weight:800;font-size:13px;line-height:1.25;text-align:center;color:#e6ebf3;letter-spacing:.4px;border-bottom:1px solid rgba(255,255,255,.6);padding-bottom:2px}
.divider{position:absolute;top:292px;left:190px;width:1px;height:128px;background:rgba(255,255,255,.18)}
/* inside */
.lower{position:absolute;left:0;top:290px;width:380px;height:130px;background:linear-gradient(180deg,var(--slate-light),var(--slate))}
.services{left:0;top:305px;height:115px;padding:0 12px}
.plans{left:190px;top:305px;height:115px;padding:0 10px;border-left:1px solid rgba(255,255,255,.18)}
.plan-lists{display:flex;gap:6px}
.plan-lists ul{list-style:none;flex:1}
.plan-lists li{font-size:5.2px;line-height:1.9;color:#e4e4e6}
.plan-lists li::before{content:"› ";font-weight:700}
.side{left:380px;background:linear-gradient(180deg,var(--slate-dark),var(--slate));padding:12px 10px 0}
.cite{font-size:5px;text-align:right;font-weight:600;margin:-2px 0 6px;color:#f0f0f0}
.footer--wide{width:190px}
</style>
</head>
<body>

<!-- Outside of the tri-fold -->
<section class="sheet sheet--outside" aria-label="Flyer outside">
  <div class="panel about">
    <h2 class="heading">ABOUT US</h2>
    <p class="body-text">With more than 20 years combined experience in construction, T&amp;R holds itself to the highest levels of quality, material, workmanship and service in each and every project we build.</p>
    <p class="body-text">A reputation is only as good as the last referral, and we know our future relies on satisfied customers. We take the time to fully understand what each customer expects. Service is more than a trend for us; it is the philosophy behind everything we do, and our home buyers share in the benefits.</p>
    <p class="body-text">T&amp;R is committed to building quality homes with careful craftsmanship, custom designs and thoughtful touches that add to each homeowner's way of life. Over the years we have built close working ties with fine local craftsmen, vendors and suppliers across the region.</p>
    <h2 class="heading" style="margin-top:8px">OUR PARTNERS</h2>
    <div class="partner"><div class="name">Dale Harwick</div>
      <div class="phone"><svg width="6" height="6" viewBox="0 0 10 10"><circle cx="5" cy="5" r="4.3" fill="none" stroke="#fff" stroke-width="1"/><path d="M3.3 2.8l1 1-.6.7a3 3 0 0 0 1.8 1.8l.7-.6 1 1-.8.8c-1.8-.2-3.6-2-3.9-3.9z" fill="#fff"/></svg>555-014-2290</div></div>
    <div class="partner"><div class="name">Tom Renner</div>
      <div class="phone"><svg width="6" height="6" viewBox="0 0 10 10"><circle cx="5" cy="5" r="4.3" fill="none" stroke="#fff" stroke-width="1"/><path d="M3.3 2.8l1 1-.6.7a3 3 0 0 0 1.8 1.8l.7-.6 1 1-.8.8c-1.8-.2-3.6-2-3.9-3.9z" fill="#fff"/></svg>555-017-6634</div></div>
  </div>
  <div class="photo" role="img" aria-label="Completed home with a two-level wooden deck and stairs" style="left:0;top:276px;width:190px;height:144px;background:linear-gradient(180deg,#a9b3bd 0%,#8c7f72 45%,#5a3a2e 75%,#4f6a37 100%)"></div>
  <div class="footer"><span class="dot"></span>www.trhomesbuildco.example</div>

  <div class="photo" role="img" aria-label="Large brick custom home with steep gabled roofs under a pale sky" style="left:190px;top:0;width:380px;height:250px;background:linear-gradient(180deg,var(--sky-top) 0%,var(--sky-bottom) 38%,#9b6f55 55%,#7a5040 78%,#4f7a35 92%,#3f6a2c 100%)"></div>
  <div class="brand"><span class="mark"></span><span>T&amp;R Custom Homes and Remodeling</span></div>

  <div class="thumbs" style="left:198px;top:244px">
    <div class="thumb"><div class="pic" role="img" aria-label="Remodeled bathroom" style="background:linear-gradient(135deg,#3a2a22,#8a6a55)"></div>BATHROOM</div>
    <div class="thumb"><div class="pic" role="img" aria-label="Finished interior room" style="background:linear-gradient(135deg,#d8d2c6,#8e8374)"></div>OTHERS</div>
    <div class="thumb"><div class="pic" role="img" aria-label="Custom kitchen" style="background:linear-gradient(135deg,#2a3140,#c9ccd2)"></div>KITCHEN</div>
    <div class="thumb"><div class="pic" role="img" aria-label="Stone front door entry" style="background:linear-gradient(135deg,#7a6b5c,#b9ab98)"></div>FRONT DOOR</div>
  </div>

  <div class="divider"></div>
  <div class="panel contact">
    <h2>CONTACT US</h2>
    <p>(555) 014-2290</p>
    <p style="margin:5px 0 2px"><svg width="6" height="8" viewBox="0 0 10 14"><path d="M5 0a5 5 0 0 0-5 5c0 3.8 5 9 5 9s5-5.2 5-9a5 5 0 0 0-5-5zm0 7a2 2 0 1 1 0-4 2 2 0 0 1 0 4z" fill="#fff"/></svg></p>
    <p>1820 Ridgeline Road Suite 4<br>Oakfield, IL 60000</p>
  </div>
  <div class="footer" style="left:190px"><span class="dot"></span>www.trhomesbuildco.example</div>

  <div class="panel tagline"><h2>WHERE EVERY<br>DETAIL MATTERS</h2></div>
  <div class="footer" style="left:380px"><span class="dot"></span>www.trhomesbuildco.example</div>
</section>

<!-- Inside of the tri-fold -->
<section class="sheet sheet--inside" aria-label="Flyer inside">
  <div class="photo" role="img" aria-label="Homeowner family seated on the front steps of a brick home with a white porch railing" style="left:0;top:0;width:380px;height:290px;background:linear-gradient(180deg,#d9dcdf 0%,#9b5a44 30%,#7c4434 55%,#c9bfb0 75%,#4f7a35 100%)"></div>
  <div class="lower"></div>
  <div class="thumbs" style="left:8px;top:246px">
    <div class="thumb"><div class="pic" role="img" aria-label="Kitchen" style="background:linear-gradient(135deg,#2d2a28,#8d7f70)"></div>KITCHEN</div>
    <div class="thumb"><div class="pic" role="img" aria-label="Bathroom" style="background:linear-gradient(135deg,#1e2a3c,#4d6280)"></div>BATHROOM</div>
    <div class="thumb" style="margin-left:14px"><div class="pic" role="img" aria-label="Foyer with staircase" style="background:linear-gradient(135deg,#6a4f3c,#d6cbb9)"></div>FOYER</div>
    <div class="thumb"><div class="pic" role="img" aria-label="Front door" style="background:linear-gradient(135deg,#5a3c28,#e2d6bf)"></div>FRONT DOOR</div>
  </div>

  <div class="panel services">
    <h2 class="heading">SERVICES</h2>
    <p class="body-text">Let T&amp;R Homes be a part of your next construction project and you will be glad you did. Covering all construction, remodeling and building-related services, T&amp;R brings over 20 years of experience to the making of the highest quality with attention to every detail. Whether the job is big or small, we promise one-on-one service with customer satisfaction guaranteed.</p>
  </div>
  <div class="footer" style="left:0"><span class="dot"></span>www.trhomesbuildco.example</div>

  <div class="panel plans">
    <h2 class="heading">FLOOR PLANS</h2>
    <div class="plan-lists">
      <ul><li>Forge First Floor</li><li>Forge Second Floor</li><li>Forge Front Elevation</li><li>Forge Back Elevation</li><li>Forge Left Elevation</li><li>Forge Right Elevation</li></ul>
      <ul><li>Forge 2 1st Floor</li><li>Forge 2 2nd Floor</li><li>Forge 2 Front Elevation</li><li>Forge 2 Back Elevation</li><li>Forge 2 Left Elevation</li><li>Forge 2 Right Elevation</li></ul>
    </div>
  </div>
  <div class="footer" style="left:190px"><span class="dot"></span>www.trhomesbuildco.example</div>

  <div class="panel side">
    <h2 class="heading">FREE ESTIMATES</h2>
    <p class="body-text">Planning your dream home, remodeling your current one, or doing a simple addition? Rest easy knowing you are in safe and skilled hands. T&amp;R specializes in custom home building and remodeling, and our team is here to cover your every need.</p>
    <p class="body-text">T&amp;R offers fair pricing for all projects and, as a small family-owned business, we keep our costs low and pass the savings on to our customers.</p>
    <p class="body-text">For a free estimate on your next project, contact T&amp;R by filling out the form below or calling 555-014-2290. Thank you for choosing T&amp;R Custom Homes &amp; Remodeling.</p>
    <h2 class="heading" style="margin-top:6px">TESTIMONIALS</h2>
    <p class="body-text">"We had our basement finished by T&amp;R last year, and although friends highly recommended them, the work went far beyond our hopes. Their attention to detail and courtesy were superior. The basement looks fabulous and we could not be happier."</p>
    <p class="cite">- The Harlows, Millbrook IL</p>
    <p class="body-text">"Dale is highly professional in the way he runs his business and truly champions his customers. T&amp;R built us a quality home and kept every promise before and after the sale. If we ever build again, T&amp;R would be our first call."</p>
    <p class="cite">- Ken &amp; Dana Pruitt, Elmridge IL</p>
  </div>
  <div class="photo" role="img" aria-label="Stone and brick custom home with a lawn and a small sign in front" style="left:380px;top:318px;width:190px;height:102px;background:linear-gradient(180deg,#d7e1ea 0%,#b4c6d6 30%,#6b5344 55%,#4f7a35 80%,#3f6a2c 100%)"></div>
  <div class="footer" style="left:380px"><span class="dot"></span>www.trhomesbuildco.example</div>
</section>

</body>
</html>
```